Poster Design Project for Over 50's Gym

We need a poster design to advertise our over 50's gym. We want to attract older adults who love enjoying their age, living life and having a bit of fun.
We would like to see a bright, fun, non-intimidating poster communicating how easy exercise can be and how great it can be for your health.
I would like the poster to include the following information.
Title:
Mackay's Over 50's Gym
Exercise with confidence
How old would you be if you didn't know your age?
Suitable exercise programmes for all medical conditions
Friendly and non-intimidating environment
Private health insurance rebates
University qualified exercise physiologists
Vital Steps Exercise Physiology Clinic
Exercise Physiologists Loretta Brisbeck & Damon Ellery
Suite 7, 214 Tarlow Street, Mackay
www.vitalstepsclinic.com.au
MON - FRI 8:30 am - 6:30 pm
I have photos available for use & Logo just unable to attach at moment****
Over 50 adult
Medical

```html
<!DOCTYPE html>
<html lang="en">
<head>
<meta charset="utf-8">
<title>Mackay's Over 50's Gym – Poster</title>
<link rel="stylesheet" href="https://fonts.googleapis.com/css2?family=Arvo:wght@700&family=Montserrat:wght@800&family=PT+Sans:wght@400;700&display=swap">
<style>
  :root {
    --navy: #1f3566;
    --orange: #f26522;
    --orange-glow: #f47a3c;
    --slate: #7b838c;
    --ink: #231f20;
    --white: #ffffff;
    --pink: #f4b8c6;
    --sky: #d4ebf5;
    --grey-wash: #b9b3bb;
    --page: #ffffff;
  }
  * { margin: 0; padding: 0; box-sizing: border-box; }
  html, body { width: 1200px; height: 1000px; overflow: hidden; background: var(--page); }
  body { position: relative; font-family: "PT Sans", Arial, sans-serif; }

  .poster {
    position: absolute; left: 316px; top: 48px;
    width: 567px; height: 802px;
    background: var(--white);
    border: 1px solid #8a8a8a;
    overflow: hidden;
  }

  .brush-backdrop {
    position: absolute; left: 0; top: 0; width: 567px; height: 480px;
  }

  .clinic-mark {
    position: absolute; left: 24px; top: 24px; width: 156px; height: 38px;
    background: var(--white);
    display: flex; align-items: center; gap: 6px; padding: 0 8px;
  }
  .clinic-mark .dot { width: 14px; height: 14px; border-radius: 50%; background: var(--orange); flex: none; }
  .clinic-mark .name { font-weight: 700; font-size: 10.5px; line-height: 1.1; color: var(--navy); }

  .headline { position: absolute; left: 0; top: 0; width: 567px; height: 400px; }
  .headline span { position: absolute; white-space: nowrap; line-height: 1; }
  .slab {
    font-family: "Arvo", Rockwell, serif; font-weight: 700; color: var(--navy);
    text-shadow:
      -2px -2px 0 var(--white), 2px -2px 0 var(--white), -2px 2px 0 var(--white), 2px 2px 0 var(--white),
      0 -2px 0 var(--white), 0 2px 0 var(--white), -2px 0 0 var(--white), 2px 0 0 var(--white),
      0 0 8px var(--orange-glow), 0 0 14px var(--orange-glow), 4px 5px 6px rgba(0,0,0,.35);
  }
  .headline .mackays { left: 100px; top: 132px; font-size: 70px; letter-spacing: -1px; }
  .headline .over { left: 52px; top: 196px; font-size: 58px; letter-spacing: -1px; }
  .headline .gym { left: 350px; top: 318px; font-size: 58px; letter-spacing: -1px; }
  .headline .fifties {
    left: 205px; top: 218px; font-family: "Montserrat", "Arial Black", sans-serif; font-weight: 800;
    font-size: 128px; letter-spacing: -4px; color: var(--white);
    text-shadow:
      -2px -2px 0 var(--orange), 2px -2px 0 var(--orange), -2px 2px 0 var(--orange), 2px 2px 0 var(--orange),
      0 0 10px var(--orange-glow), 5px 6px 8px rgba(0,0,0,.45);
  }

  .members-photo { position: absolute; left: 300px; top: 434px; width: 226px; height: 282px; }

  .benefits { position: absolute; left: 30px; top: 508px; width: 250px; }
  .benefits .question { color: var(--orange); font-weight: 700; font-size: 14px; line-height: 17px; margin-bottom: 8px; }
  .benefits ul { list-style: none; }
  .benefits li {
    position: relative; padding-left: 15px; font-size: 11.5px; line-height: 14px;
    color: var(--ink); margin-bottom: 6px;
  }
  .benefits li::before {
    content: ""; position: absolute; left: 1px; top: 5px; width: 4px; height: 4px;
    border-radius: 50%; background: var(--orange);
  }

  .hours {
    position: absolute; left: 20px; top: 740px; width: 176px; text-align: center;
    color: var(--navy); font-weight: 700; font-size: 17px; line-height: 22px;
  }

  .contact-band { position: absolute; left: 210px; top: 722px; width: 357px; height: 80px; }
  .contact {
    position: absolute; left: 241px; top: 733px; font-size: 11px; line-height: 15px; color: var(--white);
  }
  .contact .clinic { font-weight: 700; }
  .contact .web { color: var(--orange); }
</style>
</head>
<body>
  <main class="poster">
    <svg class="brush-backdrop" viewBox="0 0 567 480" role="img" aria-label="Painted brush-stroke and halftone backdrop in pink, sky blue and grey">
      <defs>
        <linearGradient id="wash" x1="0" y1="0" x2="1" y2="0">
          <stop offset="0" stop-color="#c9c2c8"/>
          <stop offset=".35" stop-color="#f4b8c6"/>
          <stop offset=".7" stop-color="#f6c3cf"/>
          <stop offset="1" stop-color="#d4ebf5"/>
        </linearGradient>
        <linearGradient id="fade" x1="0" y1="0" x2="0" y2="1">
          <stop offset="0" stop-color="#fff" stop-opacity="0"/>
          <stop offset=".55" stop-color="#fff" stop-opacity="0"/>
          <stop offset="1" stop-color="#fff" stop-opacity="1"/>
        </linearGradient>
      </defs>
      <rect width="567" height="480" fill="url(#wash)"/>
      <rect width="567" height="480" fill="url(#fade)"/>
    </svg>

    <div class="clinic-mark"><span class="dot"></span><span class="name">Vital Steps<br>Exercise Physiology Clinic</span></div>

    <h1 class="headline" aria-label="Mackay's Over 50's Gym">
      <span class="slab mackays">Mackay's</span>
      <span class="slab over">Over</span>
      <span class="fifties">50's</span>
      <span class="slab gym">Gym</span>
    </h1>

    <svg class="members-photo" viewBox="0 0 226 282" role="img" aria-label="Photo of an older woman and man standing beside an elliptical trainer">
      <defs>
        <linearGradient id="photo" x1="0" y1="0" x2="0" y2="1">
          <stop offset="0" stop-color="#eef2f5"/>
          <stop offset="1" stop-color="#c9cdd2"/>
        </linearGradient>
      </defs>
      <rect width="226" height="282" fill="url(#photo)"/>
    </svg>

    <section class="benefits">
      <p class="question">How old would you be if you didn't know your age?</p>
      <ul>
        <li>Suitable exercise programmes for all medical conditions</li>
        <li>Friendly and non-intimidating environment</li>
        <li>Private health insurance rebates</li>
        <li>University qualified exercise physiologists</li>
      </ul>
    </section>

    <p class="hours">MON - FRI<br>8:30 am - 6:30 pm</p>

    <svg class="contact-band" viewBox="0 0 357 80" aria-hidden="true">
      <polygon points="18,0 357,0 357,80 0,80" fill="var(--slate)"/>
    </svg>
    <address class="contact" style="font-style:normal">
      <div class="clinic">Vital Steps Exercise Physiology Clinic</div>
      <div>Exercise Physiologists Loretta Brisbeck &amp; Damon Ellery</div>
      <div>Suite 7, 214 Tarlow Street, Mackay</div>
      <div class="web">www.vitalstepsclinic.com.au</div>
    </address>
  </main>
</body>
</html>
```